Business card and (possibly) logo

Hi - we need a new business card.
We have an existing logo that we quite like but we are open to options.
We are an architectural firm - we specialize in upmarket residential work and apartment blocks.
We are chasing a business card at present but also want to extensively update our website going forward to attract a much higher level of client / investor / developer.
Our current logo is black, grey and yellow and based on the sun/moon temples in Mexico.
We are open to variations.
We want to communicate professionalism, trust, quality.
Our website is www.korvalstudio.com.au - but note as above - we want to change the website as well to be a lot 'classier' and to appeal to a higher end market.

thanks

Target Market(s)

We are an architect firm - our target market is Developers and builders of high end houses and luxury apartment blocks. Also private home owners wanting to build excellent expensive houses. (ideally over $1m budgets)

Industry/Entity Type

Residential

Requirements
Must have
• Logo
Contact details;
Name
phone, mobile, email, web

```html
<!DOCTYPE html>
<html lang="en">
<head>
<meta charset="utf-8">
<title>Korval Studio – Business Card</title>
<link rel="stylesheet" href="https://fonts.googleapis.com/css2?family=Questrial&display=swap">
<style>
  :root {
    --page: #ffffff;
    --card-dark: #4f4c49;
    --ink-dark: #dcd3c4;
    --rule-dark: #6a6661;
    --card-light: #ffffff;
    --ink-light: #a9a49d;
    --rule-light: #e2ded8;
    --frame-beige: #c9bb9f;
    --frame-grey: #b9b5af;
    --sun: #cdbb9c;
  }
  * { box-sizing: border-box; margin: 0; padding: 0; }
  html, body {
    width: 1008px;
    height: 1200px;
    overflow: hidden;
    background: var(--page);
    font-family: "Questrial", Arial, sans-serif;
  }
  .canvas {
    position: relative;
    width: 1008px;
    height: 1200px;
  }
  .card {
    position: absolute;
    left: 36px;
    width: 950px;
    height: 540px;
    font-variant: small-caps;
    text-transform: none;
  }
  .card--dark {
    top: 8px;
    background: var(--card-dark);
    color: var(--ink-dark);
    --rule: var(--rule-dark);
  }
  .card--light {
    top: 650px;
    background: var(--card-light);
    color: var(--ink-light);
    border: 1.5px solid var(--frame-grey);
    --rule: var(--rule-light);
  }
  .outer-frame {
    position: absolute;
    left: 18px;
    top: 634px;
    width: 985px;
    height: 560px;
    border: 3px solid var(--frame-beige);
  }
  .brand {
    position: absolute;
    left: 38px;
    top: 70px;
    width: 410px;
  }
  .brand__mark {
    width: 84px;
    height: 84px;
    border-radius: 50%;
    background: var(--sun);
    margin-bottom: 40px;
  }
  .brand__name {
    font-size: 60px;
    line-height: 1.05;
    letter-spacing: 6px;
    font-variant: normal;
    text-transform: uppercase;
    color: inherit;
  }
  .divider {
    position: absolute;
    left: 477px;
    top: 78px;
    width: 1.5px;
    height: 366px;
    background: var(--rule);
  }
  .contact {
    position: absolute;
    left: 513px;
    top: 220px;
    list-style: none;
    font-size: 26px;
    letter-spacing: 2.5px;
    line-height: 38px;
  }
  .address {
    position: absolute;
    left: 26px;
    right: 20px;
    top: 462px;
    font-size: 25px;
    letter-spacing: 3.2px;
    white-space: nowrap;
  }
</style>
</head>
<body>
<main class="canvas">

  <section class="card card--dark" aria-label="Business card, dark version">
    <div class="brand">
      <div class="brand__mark"></div>
      <p class="brand__name">Korval<br>Studio</p>
    </div>
    <div class="divider"></div>
    <ul class="contact">
      <li>Adam Reyes</li>
      <li>Serior Architech</li>
      <li>002-555-014-2730</li>
      <li>Adam@KorvalStudio.com</li>
    </ul>
    <p class="address">4410 Marlow Lane – Denford, Australia 90214</p>
  </section>

  <div class="outer-frame"></div>
  <section class="card card--light" aria-label="Business card, light version">
    <div class="brand">
      <div class="brand__mark"></div>
      <p class="brand__name">Korval<br>Studio</p>
    </div>
    <div class="divider"></div>
    <ul class="contact">
      <li>Adam Reyes</li>
      <li>Serior Architech</li>
      <li>002-555-014-2730</li>
      <li>Adam@KorvalStudio.com</li>
    </ul>
    <p class="address">4410 Marlow Lane – Denford, Australia 90214</p>
  </section>

</main>
</body>
</html>
```